quillora.link quillora.space quillora.press website

The website is named QUILLORA and it will have 3 domain names. quillora.link, press, space.
I'd like it to be viewed on Pads, pcs and phones.

page menu:

quillora.link(start page): presentation of company. (creative, design, app, new product innovation.)
Here we'll need sosial media icons: twitter, instagram, facebook, linkedin. (light but some 'fruity' colors)

quillora.press: blog. It will be a 75% picture blog > rest will be text. I need to be able to resize pictures and shape columns to picture size. (light but some 'fruity' colors)

quillora.space : the fun part of this web design, however, on entering the page I'd like a non-disclosure agreement where viewer simply click "yes, I agree" after filling out contact info. (check attached document)
We will have space here for uploading PDF files viewers can download. There is also a blog space here to tell in brief about the PDF file. (maybe a space/sci-fi theme her e.g spacechimp, Laika the space dog?)

I will attach the logo here I want you to use > and develop for the .space .press webpage. The logo i uploaded is for the .link page.

Target Market(s)

venture capitalists

Number of Pages Required

3 page

Requirements
Must have
• a few 'fruity colors' but mostly white and grey

```html
<!DOCTYPE html>
<html lang="en">
<head>
<meta charset="utf-8">
<title>Quillora Link</title>
<link rel="stylesheet" href="https://fonts.googleapis.com/css2?family=Dosis:wght@500;600&family=Noto+Serif&family=Open+Sans:ital,wght@0,400;0,700;1,600&family=Arimo:wght@400;700&display=swap">
<style>
:root{
  --green:#4f9139;
  --green-dark:#2f6e2b;
  --green-circle:#3f8a34;
  --red:#e04a35;
  --red-band:#d4493b;
  --grey-bar:#eceeef;
  --grey-line:#e2e2e2;
  --text:#333;
  --white:#fff;
}
*{margin:0;padding:0;box-sizing:border-box}
html,body{width:858px;height:1200px;overflow:hidden;background:var(--white)}
body{position:relative;font-family:'Arimo',Arial,sans-serif;color:var(--text)}
.abs{position:absolute}

/* header */
.top-bar{left:0;top:0;width:858px;height:26px}
.contact-item{top:6px;font-size:10.5px;color:#555;display:flex;align-items:center;gap:6px}
.contact-email{left:464px}
.contact-phone{left:606px}
.social{top:5px;left:717px;display:flex;gap:5px}
.social span{width:16px;height:16px;background:var(--red);display:block}
.brand{left:64px;top:4px;width:90px}
.brand-name{font-family:'Open Sans',sans-serif;font-weight:700;font-size:17px;color:#111;letter-spacing:.5px}
.brand-mark{width:30px;height:30px;background:var(--red);margin-top:4px}
.nav{top:26px;left:450px;display:flex;height:30px;font-size:10.5px}
.nav a{color:#333;text-decoration:none;display:flex;align-items:center;padding:0 18px;position:relative}
.nav a.active{background:var(--green);color:var(--white);width:64px;justify-content:center;padding:0}
.nav a+a:not(:nth-child(2))::before{content:"";position:absolute;left:0;top:12px;height:8px;border-left:1px solid #ccc}

/* hero */
.hero{left:0;top:56px;width:858px;height:397px;background:linear-gradient(180deg,#5e7d9a 0%,#8fa6bb 45%,#b6c4d0 75%,#9fb1c1 100%)}
.hero-title{right:64px;top:124px;text-align:right;font-family:'Noto Serif',serif;font-size:30px;line-height:43px;color:var(--white);text-shadow:0 1px 3px rgba(0,0,0,.35)}
.btn-contact{left:665px;top:321px;width:131px;height:32px;background:var(--red);color:var(--white);font-family:'Open Sans',sans-serif;font-weight:700;font-size:13px;display:flex;align-items:center;justify-content:center;border-bottom:3px solid #9f2e20;border-radius:2px}

/* headings */
.section-title{left:0;width:858px;text-align:center;font-family:'Dosis',sans-serif;font-weight:500;font-size:25px;color:var(--green-dark)}
.section-title em{font-style:normal;color:var(--red)}
.rule{left:288px;width:290px;height:1px;background:var(--grey-line)}
.rule-accent{left:408px;width:49px;height:3px;background:var(--green)}

.intro{left:68px;top:541px;width:722px;text-align:center;font-size:10.6px;line-height:16px;color:#222}
.intro p+p{margin-top:6px}
.read-more{left:0;top:642px;width:858px;text-align:center;font-size:9.5px;font-weight:700;text-decoration:underline;color:#111}

/* band */
.band{left:0;top:697px;width:858px;height:122px;background:linear-gradient(180deg,#d8503f,#cc4436)}
.band-text{left:0;top:727px;width:858px;text-align:center;font-family:'Open Sans',sans-serif;font-style:italic;font-weight:600;font-size:19px;line-height:34px;color:var(--white);text-shadow:0 1px 2px rgba(0,0,0,.3)}

/* services */
.service{top:920px;width:190px;text-align:center}
.service-icon{width:84px;height:84px;margin:0 auto;border:3px solid var(--green-circle);border-radius:50%;padding:4px}
.service-icon div{width:100%;height:100%;background:var(--green-circle);border-radius:50%;display:flex;align-items:center;justify-content:center}
.service h3{font-weight:400;font-size:13.5px;margin-top:10px;color:#222}
.service p{font-size:10.5px;line-height:16px;margin-top:6px;color:#333}
.service-card{left:242px;top:907px;width:186px;height:195px}
.service.active{color:var(--white)}
.service.active h3,.service.active p{color:var(--white)}
.service.active .service-icon{border-color:var(--green-dark)}
.service.active .service-icon div{background:var(--green-dark)}

/* footer */
.footer{left:0;top:1134px;width:858px;height:66px}
.copyright{left:63px;top:1170px;font-size:8px;color:var(--white)}
.footer-brand{left:700px;top:1146px;font-family:'Open Sans',sans-serif;font-weight:700;font-size:14px;color:#111}
</style>
</head>
<body>

<svg class="abs top-bar" width="858" height="72" viewBox="0 0 858 72" aria-hidden="true">
  <polygon points="260,0 858,0 858,26 234,26" fill="var(--grey-bar)"/>
</svg>

<div class="abs contact-item contact-email">
  <svg width="13" height="9" viewBox="0 0 13 9"><rect width="13" height="9" fill="var(--red)"/><polyline points="0,0 6.5,5 13,0" fill="none" stroke="#fff" stroke-width="1"/></svg>
  hello@quillora.link
</div>
<div class="abs contact-item contact-phone">
  <svg width="16" height="16" viewBox="0 0 16 16"><circle cx="8" cy="8" r="7" fill="none" stroke="var(--red)" stroke-width="1.3"/><path d="M5 4.5c0 3.5 2.5 6.5 6 7l1-1.5-2-1-1 1c-1-.5-2-1.5-2.5-2.5l1-1-1-2z" fill="var(--red)"/></svg>
  (123) 555 0142
</div>
<div class="abs social" aria-label="Social links"><span></span><span></span><span></span><span></span></div>

<div class="abs brand">
  <div class="brand-name">QUILLORA</div>
  <div class="brand-mark"></div>
</div>

<nav class="abs nav">
  <a class="active">Home</a><a>About</a><a>Services</a><a>Our Work</a><a>Contact</a>
</nav>

<div class="abs hero" role="img" aria-label="Photo of a hand holding a smartphone in front of a city skyline rising above the fog"></div>
<svg class="abs" style="left:0;top:56px" width="858" height="16" viewBox="0 0 858 16" aria-hidden="true">
  <polygon points="0,0 205,0 190,14 0,14" fill="#fff"/>
  <line x1="205" y1="0.5" x2="858" y2="0.5" stroke="#d5d5d5"/>
</svg>

<h1 class="abs hero-title">Lorem Ipsum Dolor Sit Amet<br>Consectetuer Adipiscing Elit Sed<br>Diam Nonummy Nibh</h1>
<div class="abs btn-contact">CONTACT NOW !</div>

<h2 class="abs section-title" style="top:484px">Welcome to <em>Quillora Link</em></h2>
<div class="abs rule" style="top:524px"></div>
<div class="abs rule-accent" style="top:522px"></div>

<div class="abs intro">
  <p>Lorem ipsum dolor sit amet, consectetuer adipiscing elit, sed diam nonummy nibh euismod tincidunt ut laoreet dolore magna aliquam erat volutpat. Ut wisi enim ad minim veniam, quis nostrud exerci tation ullamcorper suscipit lobortis nisl ut aliquip ex ea commodo consequat. Duis autem vel eum iriure dolor in hendrerit in vulputate velit esse molestie consequat, vel illum dolore eu feugiat nulla facilisis at vero eros et accumsan et iusto odio dignissim qui blandit praesent luptatum zzril delenit augue duis dolore te feugait nulla facilisi.</p>
  <p>We are committed to providing our customers with quality products, designs and 100% Work Satisfaction</p>
</div>
<div class="abs read-more">Read More</div>

<div class="abs band" role="img" aria-label="Red tinted photo of business people in an office"></div>
<p class="abs band-text">We Strive To Out Work Our Competition With An Effective Approach And A Powerful<br>Skill Set, Which Is Why Were Industry Leading.</p>

<h2 class="abs section-title" style="top:832px">Our <em>Services</em></h2>
<div class="abs rule" style="top:866px"></div>
<div class="abs rule-accent" style="top:864px"></div>

<svg class="abs service-card" viewBox="0 0 186 195" aria-hidden="true">
  <polygon points="0,0 155,0 186,31 186,195 25,195 0,170" fill="var(--green)"/>
</svg>

<div class="abs service" style="left:51px">
  <div class="service-icon"><div>
    <svg width="34" height="34" viewBox="0 0 34 34"><circle cx="17" cy="8" r="4" fill="#fff"/><circle cx="17" cy="17" r="5" fill="#fff"/><path d="M6 31c1-7 5-9 11-9s10 2 11 9z" fill="#fff"/></svg>
  </div></div>
  <h3>Creative</h3>
  <p>Lorem ipsum dolor sit amet,<br>consectetuer adipiscing elit, sed<br>diam nonummy nibh.</p>
</div>

<div class="abs service active" style="left:240px">
  <div class="service-icon"><div>
    <svg width="34" height="34" viewBox="0 0 34 34"><rect x="5" y="6" width="18" height="22" rx="2" fill="none" stroke="#fff" stroke-width="2"/><rect x="19" y="14" width="9" height="15" rx="1.5" fill="#fff"/><circle cx="12" cy="15" r="3" fill="#fff"/></svg>
  </div></div>
  <h3>App Development</h3>
  <p>Lorem ipsum dolor sit amet,<br>consectetuer adipiscing elit, sed<br>diam nonummy nibh.</p>
</div>

<div class="abs service" style="left:438px">
  <div class="service-icon"><div>
    <svg width="34" height="34" viewBox="0 0 34 34"><circle cx="10" cy="10" r="4" fill="none" stroke="#fff" stroke-width="2.5" stroke-dasharray="2 1.5"/><circle cx="20" cy="8" r="3" fill="none" stroke="#fff" stroke-width="2" stroke-dasharray="1.5 1.2"/><path d="M14 31v-6c-3-1-4-4-4-7 0-4 3-6 7-6s7 3 7 6l2 4h-2v4h-4v5z" fill="#fff"/></svg>
  </div></div>
  <h3>New Product Innovations</h3>
  <p>Lorem ipsum dolor sit amet,<br>consectetuer adipiscing elit, sed<br>diam nonummy nibh.</p>
</div>

<div class="abs service" style="left:628px">
  <div class="service-icon"><div>
    <svg width="34" height="34" viewBox="0 0 34 34"><rect x="4" y="7" width="26" height="17" fill="none" stroke="#fff" stroke-width="2.5"/><rect x="14" y="24" width="6" height="4" fill="#fff"/><rect x="10" y="28" width="14" height="2" fill="#fff"/><line x1="11" y1="20" x2="24" y2="5" stroke="#fff" stroke-width="2.5"/></svg>
  </div></div>
  <h3>Design</h3>
  <p>Lorem ipsum dolor sit amet,<br>consectetuer adipiscing elit, sed<br>diam nonummy nibh.</p>
</div>

<svg class="abs footer" viewBox="0 0 858 66" aria-hidden="true">
  <polygon points="0,21 648,21 668,1 858,1 858,66 0,66" fill="var(--green)"/>
  <polygon points="0,24 650,24 670,4 858,4 858,66 0,66" fill="var(--red)"/>
</svg>
<div class="abs copyright">Copyright© 2016 &nbsp;Quillora Link &nbsp;All rights reserved</div>
<div class="abs footer-brand">QUILLORA</div>

</body>
</html>
```